Stationary, Envelope, Folder, Brochure
brightmendhome.example
Stationary, Envelope, Folder, Brochure - Health
Creative Brief
Health
Corporate, and Patients. Something bright and uplifting to grab the brightmend home feeling when people look at our materials. I like the QVR Petal Courier Lad logo and some of the materials they use. It has an uplifting look and feel.
Provide the materials listed in the Title. Use the uploaded picture logo.
quietharborwatch quietharborwatch
Colors: I do like the Blues and the gradient from a darker to a brighter blue. Maybe even do that more with other bright colors. Have fun explore a little and think outside the box. Will try to provide with as much feedback as possible. -Desmond
Hi Everyone, Keep in mind we want a look and feel of "BRIGHT Mend Home" and putting the "Care" back into healthcare. Having a bright and professional look that will excite the senses when a person looks at the material. We do not want to be the "norm" of home health. Our clients are of all ages for example 20+. Lets get excited, creative, and see what we can come up with. Also "Brightmend Home" Font needs to also be fun and represent the logo and spirit of the great experience our company provide unlike others.

```html
<!DOCTYPE html>
<html lang="en">
<head>
<meta charset="utf-8">
<title>Brightmend Home – Stationery, Envelope, Folder, Brochure</title>
<link href="https://fonts.googleapis.com/css2?family=Open+Sans:wght@400;600;700&family=Dancing+Script:wght@600&display=swap" rel="stylesheet">
<style>
  :root{
    --bg:#cbcbcb;
    --paper:#ffffff;
    --blue-deep:#0a4f96;
    --blue-mid:#1a7cc6;
    --blue-bright:#38b6e8;
    --green:#8cc63f;
    --green-deep:#4f9a2a;
    --orange:#f7941d;
    --ink:#4a4a4a;
    --label:#7a7a7a;
    --sky:#cfe9f7;
    --meadow:#a8d46a;
  }
  *{box-sizing:border-box;margin:0;padding:0}
  html,body{width:1200px;height:389px;overflow:hidden;background:var(--bg)}
  body{font-family:"Open Sans",Arial,sans-serif;color:var(--ink);position:relative}
  .label{position:absolute;font-size:7px;letter-spacing:.08em;text-transform:uppercase;color:var(--label);font-weight:600}
  .sheet{position:absolute;background:var(--paper);overflow:hidden;box-shadow:0 1px 3px rgba(0,0,0,.25)}
  .wave{position:absolute;left:0;width:100%;display:block}
  .wave--bottom{bottom:0}
  .wave--top{top:0;transform:scaleY(-1)}
  .logo{display:flex;align-items:center;gap:4px;font-weight:700;color:var(--blue-mid);white-space:nowrap}
  .logo__dot{width:1em;height:1em;border-radius:50%;background:var(--blue-bright);flex:none}
  .photo{position:absolute;background:linear-gradient(180deg,var(--sky) 0%,#e8f4fb 45%,var(--meadow) 100%)}
  .tagline{font-family:"Dancing Script",cursive;color:var(--green-deep)}
  .small{font-size:5px;line-height:1.5}
  .heading{font-size:7px;font-weight:700;color:var(--blue-mid)}
  .rule{height:1px;background:#d6d6d6;margin:3px 0}
  .card{position:absolute;overflow:hidden;box-shadow:0 1px 3px rgba(0,0,0,.25)}
  .envelope{position:absolute;width:280px;height:58px;background:var(--paper);overflow:hidden;box-shadow:0 1px 3px rgba(0,0,0,.3)}
</style>
</head>
<body>

<svg width="0" height="0" style="position:absolute" aria-hidden="true">
  <defs>
    <linearGradient id="grad-blue" x1="0" x2="1" y1="0" y2="0">
      <stop offset="0" stop-color="#0a4f96"/><stop offset="1" stop-color="#38b6e8"/>
    </linearGradient>
    <linearGradient id="grad-green" x1="0" x2="1">
      <stop offset="0" stop-color="#4f9a2a"/><stop offset="1" stop-color="#b7dc55"/>
    </linearGradient>
    <linearGradient id="grad-orange" x1="0" x2="1">
      <stop offset="0" stop-color="#e4650f"/><stop offset="1" stop-color="#fbb03b"/>
    </linearGradient>
    <symbol id="band" viewBox="0 0 100 20" preserveAspectRatio="none">
      <path d="M0 9 C30 2 60 18 100 6 L100 20 L0 20Z" fill="url(#grad-blue)"/>
      <path d="M0 8 C30 0 60 16 100 4" stroke="url(#grad-green)" stroke-width="1.6" fill="none"/>
    </symbol>
  </defs>
</svg>

<!-- Labels -->
<span class="label" style="left:60px;top:6px">Brochure</span>
<span class="label" style="left:215px;top:6px">Brochure inside</span>
<span class="label" style="left:615px;top:6px">Folder</span>
<span class="label" style="left:728px;top:6px">Original card</span>
<span class="label" style="left:930px;top:6px">Letterhead</span>
<span class="label" style="left:1100px;top:6px">Fax sheet</span>
<span class="label" style="left:30px;top:183px">Flyer</span>
<span class="label" style="left:118px;top:183px">Mailer postcard</span>
<span class="label" style="left:740px;top:220px">Vertical cards</span>

<!-- Brochure cover -->
<section class="sheet brochure-cover" style="left:10px;top:18px;width:152px;height:152px">
  <div class="photo" role="img" aria-label="Photo of a happy family in a sunny meadow" style="left:0;top:0;width:152px;height:100px"></div>
  <svg class="wave wave--top" style="height:14px"><use href="#band"/></svg>
  <div class="logo" style="position:absolute;left:12px;top:110px;font-size:10px"><span class="logo__dot"></span>Brightmend Home</div>
  <div class="tagline" style="position:absolute;left:12px;top:126px;font-size:9px">Bright care, right at home</div>
  <svg class="wave wave--bottom" style="height:16px"><use href="#band"/></svg>
</section>

<!-- Brochure inside -->
<section class="sheet brochure-inside" style="left:168px;top:18px;width:172px;height:152px">
  <div class="photo" role="img" aria-label="Photo of a caregiver with an elderly couple" style="left:0;top:0;width:57px;height:70px"></div>
  <div style="position:absolute;left:62px;top:8px;width:50px">
    <div class="heading">Our Services</div>
    <div class="rule"></div>
    <p class="small">Nursing, therapy and daily support for all ages.</p>
  </div>
  <div class="photo" role="img" aria-label="Photo of a smiling child outdoors" style="left:115px;top:0;width:57px;height:70px"></div>
  <div style="position:absolute;left:8px;top:80px;width:100px">
    <div class="heading">Why Choose Us</div>
    <div class="rule"></div>
    <p class="small">Friendly staff who treat you like family.</p>
  </div>
  <svg class="wave wave--bottom" style="height:18px"><use href="#band"/></svg>
</section>

<!-- Flyer -->
<section class="sheet flyer" style="left:10px;top:194px;width:72px;height:172px">
  <div class="photo" role="img" aria-label="Photo of a group of children jumping on grass" style="left:0;top:0;width:72px;height:90px"></div>
  <div class="logo" style="position:absolute;left:5px;top:96px;font-size:6px"><span class="logo__dot"></span>Brightmend Home</div>
  <div class="heading" style="position:absolute;left:5px;top:110px">Care That Lifts You</div>
  <p class="small" style="position:absolute;left:5px;top:124px">Call us today</p>
  <svg class="wave wave--bottom" style="height:14px"><use href="#band"/></svg>
</section>

<!-- Mailer postcard -->
<section class="sheet postcard" style="left:88px;top:194px;width:132px;height:166px">
  <svg class="wave wave--top" style="height:14px"><use href="#band"/></svg>
  <div class="heading" style="position:absolute;left:8px;top:22px;color:var(--green-deep)">Welcome Home</div>
  <p class="small" style="position:absolute;left:8px;top:34px;width:70px">We bring care to your door.</p>
  <div class="photo" role="img" aria-label="Photo of a nurse visiting a patient" style="left:84px;top:20px;width:40px;height:52px"></div>
  <div class="logo" style="position:absolute;left:8px;top:130px;font-size:7px"><span class="logo__dot"></span>Brightmend Home</div>
  <p class="small" style="position:absolute;left:8px;top:142px">brightmendhome.example</p>
  <svg class="wave wave--bottom" style="height:12px"><use href="#band"/></svg>
</section>

<!-- Folder closed -->
<section class="sheet folder-closed" style="left:350px;top:14px;width:368px;height:204px">
  <div style="position:absolute;left:184px;top:0;width:184px;height:204px;background:linear-gradient(180deg,var(--blue-deep),var(--blue-bright) 55%,var(--paper) 56%)"></div>
  <div class="logo" style="position:absolute;left:226px;top:68px;font-size:11px;color:var(--paper)"><span class="logo__dot" style="background:var(--paper)"></span>Brightmend Home</div>
  <div class="tagline" style="position:absolute;left:198px;top:128px;font-size:10px;width:160px;text-align:center">Putting the Care back into health care</div>
  <p class="small" style="position:absolute;left:24px;top:170px">brightmendhome.example</p>
  <svg class="wave wave--bottom" style="height:22px"><use href="#band"/></svg>
</section>

<!-- Folder open -->
<section class="sheet folder-open" style="left:350px;top:226px;width:368px;height:152px">
  <div style="position:absolute;left:183px;top:0;width:2px;height:152px;background:#e3e3e3"></div>
  <svg style="position:absolute;left:0;top:70px" width="368" height="82" viewBox="0 0 368 82" aria-hidden="true">
    <path d="M4 30 L120 0 L180 6 L180 80 L4 80Z" fill="#f4f4f4" stroke="#dcdcdc"/>
    <path d="M188 6 L248 0 L364 30 L364 80 L188 80Z" fill="#f4f4f4" stroke="#dcdcdc"/>
    <rect x="300" y="40" width="40" height="22" fill="none" stroke="#d0d0d0"/>
  </svg>
  <svg class="wave wave--bottom" style="height:14px"><use href="#band"/></svg>
</section>

<!-- Business cards -->
<article class="card biz-front" style="left:726px;top:20px;width:86px;height:50px;background:var(--paper)">
  <div class="logo" style="position:absolute;left:6px;top:8px;font-size:6px"><span class="logo__dot"></span>Brightmend Home</div>
  <p class="small" style="position:absolute;left:6px;top:20px;font-weight:600">Desmond Reyes</p>
  <p class="small" style="position:absolute;left:6px;top:27px">Director of Care</p>
  <p class="small" style="position:absolute;left:6px;top:34px">(555) 014-2290</p>
  <svg class="wave wave--bottom" style="height:8px"><use href="#band"/></svg>
</article>
<article class="card biz-back" style="left:818px;top:20px;width:86px;height:50px;background:linear-gradient(90deg,var(--blue-deep),var(--blue-bright))">
  <div class="logo" style="position:absolute;left:14px;top:20px;font-size:7px;color:var(--paper)"><span class="logo__dot" style="background:var(--paper)"></span>Brightmend Home</div>
</article>
<article class="card biz-back-green" style="left:726px;top:78px;width:86px;height:50px;background:linear-gradient(90deg,var(--green-deep),var(--green))"></article>
<article class="card biz-back-orange" style="left:818px;top:78px;width:86px;height:50px;background:linear-gradient(90deg,#e4650f,var(--orange))"></article>

<!-- Vertical cards -->
<article class="card vcard" style="left:726px;top:232px;width:40px;height:96px;background:linear-gradient(180deg,var(--blue-deep),var(--blue-bright))"></article>
<article class="card vcard" style="left:771px;top:232px;width:40px;height:96px;background:var(--paper)">
  <svg class="wave wave--bottom" style="height:12px"><use href="#band"/></svg>
</article>
<article class="card vcard" style="left:816px;top:232px;width:40px;height:96px;background:linear-gradient(180deg,var(--green-deep),var(--green))"></article>
<article class="card vcard" style="left:861px;top:232px;width:40px;height:96px;background:linear-gradient(180deg,#e4650f,var(--orange))"></article>

<!-- Letterhead -->
<section class="sheet letterhead" style="left:912px;top:18px;width:148px;height:200px">
  <div class="logo" style="position:absolute;left:10px;top:12px;font-size:7px"><span class="logo__dot"></span>Brightmend Home</div>
  <p class="small" style="position:absolute;left:10px;top:40px">Dear Friend,</p>
  <p class="small" style="position:absolute;left:10px;top:50px">Thank you for choosing us.</p>
  <svg class="wave wave--bottom" style="height:16px"><use href="#band"/></svg>
</section>

<!-- Fax sheet -->
<section class="sheet fax" style="left:1066px;top:18px;width:126px;height:200px">
  <div class="logo" style="position:absolute;left:8px;top:12px;font-size:6px"><span class="logo__dot"></span>Brightmend Home</div>
  <div class="heading" style="position:absolute;right:8px;top:12px;font-size:10px">FAX</div>
  <div style="position:absolute;left:8px;top:36px;width:110px">
    <p class="small">To:</p><div class="rule"></div>
    <p class="small">From:</p><div class="rule"></div>
    <p class="small">Date:</p><div class="rule"></div>
    <p class="small">Pages:</p><div class="rule"></div>
  </div>
  <svg class="wave wave--bottom" style="height:14px"><use href="#band"/></svg>
</section>

<!-- Envelopes -->
<article class="envelope" style="left:910px;top:236px">
  <div style="position:absolute;right:0;top:0;width:90px;height:58px;background:linear-gradient(90deg,var(--green-deep),var(--green))"></div>
</article>
<article class="envelope" style="left:910px;top:270px">
  <div style="position:absolute;right:0;top:0;width:90px;height:58px;background:linear-gradient(90deg,#e4650f,var(--orange))"></div>
</article>
<article class="envelope" style="left:910px;top:306px">
  <div class="logo" style="position:absolute;left:10px;top:8px;font-size:6px"><span class="logo__dot"></span>Brightmend Home</div>
  <div style="position:absolute;right:0;top:0;width:90px;height:58px;background:linear-gradient(90deg,var(--blue-deep),var(--blue-bright))"></div>
  <svg class="wave wave--bottom" style="height:10px"><use href="#band"/></svg>
</article>

</body>
</html>
```